Law Office needs stationery design and business card

I currently have been using the same letterhead for the last 8 years. Since i 'm about to adding another location, I want to revamp my letterhead and business card. I already have a logo i'm happy with. I will upload my current letterhead, fax sheet, envelope, and logos. I need a business card also. I have 2 locations, 1 phone number, 1 fax line, website, etc. If possible and fitting with the design, I would like to keep the same information listed currently on the letterhead.

**Keep in mind, I also NEED A FAX SHEET COVER. thank you

Hello, Please submit a Gray Scale or Black and White version of your designs also, since most of the time I will be printing NON color stationery. I will seldom use a color print for my letterhead, I would like to have a color version for my benefit, however i will print in grayscale majority of the time . For the Business Card, that can just be in color. When I get my business cards they will be in color.Thank youEnrique Added Sunday, September 18, 2016

```html
<!DOCTYPE html>
<html lang="en">
<head>
<meta charset="utf-8">
<title>Harrowgate Law – Business Card</title>
<link rel="stylesheet" href="https://fonts.googleapis.com/css2?family=Cinzel:wght@400;600&family=Roboto:wght@400&display=swap">
<style>
  :root {
    --backdrop: #e2e2e2;
    --card: #ffffff;
    --ink: #1f1b19;
    --gold: #c2a264;
    --shadow: rgba(0, 0, 0, 0.18);
  }
  * { box-sizing: border-box; margin: 0; padding: 0; }
  html, body { width: 1200px; height: 900px; overflow: hidden; }
  body {
    background: var(--backdrop);
    display: flex;
    align-items: center;
    justify-content: center;
    gap: 48px;
  }
  .card {
    width: 540px;
    height: 309px;
    background: var(--card);
    box-shadow: 0 6px 18px var(--shadow);
    display: flex;
    flex-direction: column;
    align-items: center;
    position: relative;
  }
  .card--front { justify-content: center; }
  .brand-name {
    font-family: "Cinzel", serif;
    font-weight: 600;
    color: var(--gold);
    letter-spacing: 0.04em;
    white-space: nowrap;
  }
  .card--front .brand-name { font-size: 40px; }

  .card--back { padding-top: 66px; }
  .card--back .brand-name { font-size: 21px; }
  .person-name {
    font-family: "Cinzel", serif;
    font-weight: 400;
    font-size: 24px;
    color: var(--ink);
    margin-top: 16px;
    letter-spacing: 0.02em;
  }
  .person-role {
    font-family: "Cinzel", serif;
    font-size: 9px;
    color: var(--gold);
    letter-spacing: 0.08em;
    margin-top: 2px;
  }
  .contact {
    position: absolute;
    bottom: 26px;
    left: 0; right: 0;
    text-align: center;
    font-family: "Roboto", sans-serif;
    font-size: 9.5px;
    line-height: 1.65;
    letter-spacing: 0.06em;
    color: var(--ink);
  }
  .contact .label { color: var(--gold); }
</style>
</head>
<body>
  <section class="card card--front">
    <div class="brand-name">HARROWGATE LAW</div>
  </section>

  <section class="card card--back">
    <div class="brand-name">HARROWGATE LAW</div>
    <div class="person-name">JOHN DOE</div>
    <div class="person-role">MANAGER</div>
    <div class="contact">
      <p>418 Orchard Row, Suite 200, Fairbrook, PA 19071 | 96 Millbank Ave, Westmoor, PA 19028</p>
      <p><span class="label">phone</span> 555 201 7734 | <span class="label">fax</span> 555 201 7790 | John@HarrowgateLaw.com</p>
      <p>www.HarrowgateLaw.com</p>
    </div>
  </section>
</body>
</html>
```